Lead Generating Website Design

We are looking for a brand new design for our existing website.
The existing website is www.brvpartnerhub.com
The website is aimed at businesses that would like to licence the courses from our school to sell themselves.
We want the menu to be the following:
* Home
* About us
* Our Courses
* LMS Platform
* Affiliate Program
* Contact Us
We want the colour scheme to use the following design guide:
https://docvault.example/pedalforward/docs/keen_to_cycle_brand_guidelines
Like the idea of the circles and colours in the style guide for places. Want lots of white areas as well as coloured areas
An example of a nice looking site is : https://www.studyharbour.online/
MUST look good on mobile also
On the home page we want the following:
A large image with the text :
Over 450 courses written by highly qualified academics with real world experience.
The 'Join our thriving group of Affiliates - start your own online college!' section on the current website with the text and becoming an affiliate video
A section for 'see how our LMS works' with some text and a place for a video
A section for 'About BRV Remote Learning' with the text BRV Remote Learning has been providing distance education for over 40 years and have been the leader in online education for over 25 years.
Benefit from the resources and experience of one of the worlds leading course content providers.
Our highly qualified academic staff, HUGE resource library of up to date courses and cutting edge white label LMS enable our affiliates to stay well ahead of their competitors
A section for 'Free information pack' like the one on https://www.studyharbour.online/
Target Market(s)
Education providers looking to licence our courses to sell
Number of Pages Required
1 page

```html
<!DOCTYPE html>
<html lang="en">
<head>
<meta charset="utf-8">
<title>BRV Remote Learning — Affiliate Program</title>
<link href="https://fonts.googleapis.com/css2?family=Lato:wght@400;700;900&family=Montserrat:wght@600;700&family=Libre+Baskerville&family=Cinzel:wght@400&display=swap" rel="stylesheet">
<style>
:root{
  --blue:#0b4fc0;
  --blue-dark:#0a3f9a;
  --red:#f2513d;
  --yellow:#f1c14c;
  --ink:#1f2433;
  --text:#3b3f4a;
  --grey-bg:#ececec;
  --line:#9ea3ad;
  --footer:#4a4a5c;
  --white:#ffffff;
}
*{box-sizing:border-box;margin:0;padding:0}
html,body{width:1200px;height:3914px;overflow:hidden}
body{font-family:'Lato',sans-serif;color:var(--text);background:var(--white);position:relative}
section,header,footer{position:absolute;left:0;width:1200px}
.abs{position:absolute}
a{text-decoration:none}
.btn{position:absolute;display:flex;align-items:center;justify-content:center;font-family:'Lato',sans-serif;font-weight:700;font-size:11px;text-transform:uppercase;letter-spacing:.3px;color:var(--white);text-decoration:none}
.btn--red{background:var(--red);box-shadow:0 0 0 2px var(--white),0 0 0 3px var(--red)}
.btn--blue{background:var(--blue);box-shadow:0 0 0 2px var(--white),0 0 0 3px var(--blue)}
.heading{position:absolute;font-family:'Montserrat',sans-serif;font-weight:700;color:var(--blue);text-transform:uppercase;font-size:22px;line-height:31px;white-space:nowrap}
.center{left:0;width:1200px;text-align:center}
.body-copy{font-size:11px;line-height:19px;color:var(--ink)}

/* header */
.site-header{top:0;height:58px;background:var(--white);border-bottom:1px solid #d4d4d4}
.brand{left:161px;top:9px;width:135px;color:var(--blue);font-family:'Lato',sans-serif;font-weight:700;font-size:10px;line-height:13px;text-transform:uppercase;display:flex;gap:5px;align-items:flex-start}
.brand__mark{width:10px;height:10px;background:var(--blue);flex:none;margin-top:1px}
.nav a{position:absolute;top:22px;font-size:11px;color:var(--ink);text-transform:uppercase;letter-spacing:.2px}
.nav a.is-active{color:var(--blue)}
.nav a.is-active::after{content:"";position:absolute;left:0;right:0;top:17px;height:2px;background:var(--blue)}
.nav a.btn{left:911px;top:11px;width:126px;height:36px;font-size:10.5px;color:var(--white)}

/* hero */
.hero{top:58px;height:534px;background:linear-gradient(90deg,#b7a99c 0%,#9c8d84 28%,#a59a92 50%,#8e8580 100%);overflow:hidden}
.hero__photo{position:absolute;inset:0;background:radial-gradient(ellipse 200px 300px at 230px 300px,rgba(228,120,92,.75),rgba(228,120,92,0) 70%)}
.hero__title{left:629px;top:155px;font-family:'Libre Baskerville',serif;font-weight:400;font-size:22px;line-height:32px;color:var(--white);text-transform:uppercase;white-space:nowrap}
.hero__sub{left:629px;top:258px;width:430px;font-size:19px;line-height:27px;color:var(--white);font-weight:400}
.hero .btn{left:629px;top:329px;width:149px;height:41px;background:var(--yellow);color:#3b3a36;font-size:14px;box-shadow:none}

/* framed images */
.framed{position:absolute}
.framed__back{position:absolute;background:var(--blue)}
.framed__img{position:absolute}

/* join */
.join{top:592px;height:479px}
.join .heading{left:541px;top:58px}
.checklist{list-style:none}
.join .checklist{position:absolute;left:541px;top:166px}
.join .checklist li{position:relative;padding-left:20px;height:30px;font-size:11px;color:var(--ink)}
.join .checklist li::before{content:"";position:absolute;left:1px;top:2px;width:7px;height:7px;border:2px solid var(--red);border-radius:50%}

/* lms */
.lms{top:1071px;height:554px;background:var(--grey-bg)}
.lms__list{position:absolute;left:161px;top:222px;width:400px;list-style:none}
.lms__list li{position:relative;padding-left:35px;font-size:11px;line-height:18px;color:var(--ink);font-weight:700;margin-bottom:18px}
.lms__list svg{position:absolute;left:0;top:3px}
.video{left:605px;top:159px;width:434px;height:319px;background:var(--white);padding:10px}
.video__screen{position:relative;width:100%;height:100%;background:linear-gradient(120deg,#6d5040 0%,#9a8a7c 35%,#cfc7bb 60%,#8a7a6a 100%)}
.video__bar{position:absolute;left:0;right:0;bottom:0;height:30px;background:rgba(0,0,0,.55)}

/* who */
.who{top:1625px;height:441px}
.who .heading{left:542px;top:72px}
.who p{position:absolute;left:543px;width:420px;font-size:11px;line-height:19px;color:var(--ink)}
.who p span{color:var(--blue)}

/* interested */
.interested{top:2066px;height:299px;background:var(--grey-bg)}
.lead-form{position:absolute;left:387px;top:161px;width:438px;height:34px;background:#9b9b9b;padding:4px;display:flex;gap:6px}
.lead-form__field{flex:1;background:var(--white);display:flex;align-items:center;gap:8px;padding-left:10px;font-size:10px;color:#555}
.lead-form__submit{width:192px;background:var(--red);color:var(--white);display:flex;align-items:center;gap:8px;padding-left:10px;font-size:10px;font-weight:700}

/* why */
.why{top:2365px;height:662px}
.feature{position:absolute;top:184px;width:236px;height:91px;background:var(--white);box-shadow:0 1px 8px rgba(0,0,0,.16);display:flex;align-items:center;padding-left:22px;gap:18px}
.feature__label{font-size:14px;line-height:21px;color:var(--ink);font-weight:700}
.feature--active::after{content:"";position:absolute;left:106px;bottom:-8px;width:14px;height:14px;background:var(--white);transform:rotate(45deg);box-shadow:3px 3px 5px rgba(0,0,0,.1)}
.why__title{left:162px;top:360px;font-size:22px;font-weight:700;color:var(--red)}
.why__copy{left:162px;top:396px;width:340px;font-size:13px;line-height:22px;color:var(--ink)}
.why__image{left:536px;top:316px;width:503px;height:270px;border-radius:12px;background:linear-gradient(135deg,#d8dde0 0%,#a9b0b3 40%,#355a8c 75%,#2f6e3a 100%)}

/* contact */
.contact{top:3027px;height:553px;background:var(--grey-bg)}
.contact__title{top:82px;font-family:'Montserrat',sans-serif;font-weight:700;font-size:22px;color:var(--ink);letter-spacing:.5px}
.contact__sub{top:122px;font-size:12px;font-weight:700;color:var(--ink);text-transform:uppercase}
.field{position:absolute;height:37px;border:1px solid var(--line);display:flex;align-items:center;gap:12px;padding-left:14px;font-size:11px;color:#444}
.field--message{align-items:flex-start;padding-top:12px}

/* footer */
.site-footer{top:3580px;height:334px;background:var(--footer);color:var(--white)}
.footer-brand{top:50px;font-family:'Cinzel',serif;font-size:19px;line-height:36px;letter-spacing:2px;display:flex;flex-direction:column;align-items:center}
.footer-nav{top:166px;display:flex;justify-content:center;gap:44px;font-family:'Cinzel',serif;font-size:15px;letter-spacing:1px}
.footer-rule{left:161px;top:243px;width:878px;height:1px;background:#5d5d70}
.copyright{left:163px;top:272px;font-size:13.5px}
.socials{left:831px;top:266px;display:flex;gap:22px}
.socials span{width:28px;height:28px;border:1.5px solid var(--white);display:block}
</style>
</head>
<body>

<header class="site-header">
  <div class="abs brand"><span class="brand__mark"></span><span>BRV Remote Learning Affiliate Program</span></div>
  <nav class="nav">
    <a class="is-active" href="#" style="left:334px">Home</a>
    <a href="#" style="left:408px">About Us</a>
    <a href="#" style="left:507px">Our Courses</a>
    <a href="#" style="left:627px">LMS Platform</a>
    <a href="#" style="left:760px">Affiliate Program</a>
    <a class="btn btn--blue" href="#">Contact Us</a>
  </nav>
</header>

<section class="hero" role="img" aria-label="Photo of a smiling teacher in a coral top standing in a bright office">
  <div class="hero__photo"></div>
  <h1 class="abs hero__title">Over 450 courses written by<br>highly qualified academics<br>with real world experience.</h1>
  <p class="abs hero__sub">Join Our Thriving Group Of Affiliates Start Your Own Online College!</p>
  <a class="btn" href="#">Learn More</a>
</section>

<section class="join">
  <div class="framed" style="left:161px;top:64px">
    <div class="framed__back" style="left:0;top:14px;width:326px;height:326px"></div>
    <div class="framed__img" role="img" aria-label="Photo of a student with headphones writing at a desk" style="left:12px;top:0;width:326px;height:326px;background:linear-gradient(135deg,#e9e6e2 0%,#c9c2ba 45%,#c8302c 70%,#b5aea6 100%)"></div>
  </div>
  <h2 class="heading">Join our thriving group of affiliates<br>start your own online college!</h2>
  <p class="abs body-copy" style="left:541px;top:133px">No Previous Education Experience Required - Tutors Are Available.</p>
  <ul class="checklist">
    <li>Are You Looking For A New Business Venture?</li>
    <li>Do You Want To Be Your Own Boss?</li>
    <li>Do You Want To Earn A Great Income, And Still Have A Life?</li>
  </ul>
  <p class="abs body-copy" style="left:541px;top:256px;width:500px">You Might Already Be Working In Education, Or Perhaps You're Part Of An Association It's Offerings To It's Members, Or,That Is Looking To Expand Just A Motivated Business Person!</p>
  <p class="abs body-copy" style="left:541px;top:310px">Don't Reinvent The Wheel - Our Business Model Works - And It's An Affordable Buy In.</p>
  <a class="btn btn--red" href="#" style="left:541px;top:354px;width:124px;height:36px">Contact Us</a>
</section>

<section class="lms">
  <h2 class="heading center" style="top:70px">How our LMS works</h2>
  <p class="abs center" style="top:113px;font-size:12.5px;font-weight:700;color:var(--ink)">Lorem Ipsum Dolor Sit Amet, Consectetur Adipiscing Elit, Sed Do Eiusmod Tempor Incididunt</p>
  <p class="abs" style="left:161px;top:158px;width:420px;font-size:12.5px;line-height:21px;font-weight:700;color:var(--ink)">Lorem Ipsum Dolor Sit Amet, Consectetur Adipiscing Elit, Sed Do Incididunt Ut Labore Et Dolore Magna Aliqua</p>
  <ul class="lms__list">
    <li><svg width="18" height="16" viewBox="0 0 18 16"><rect x="1" y="3" width="12" height="12" fill="none" stroke="#f2513d" stroke-width="1.6"/><path d="M4 8l3 3 9-10" fill="none" stroke="#f2513d" stroke-width="2"/></svg>Ut Aliquip Ex Ea Commodo Consequat. Duis Aute Irure Dolor In Reprehenderit</li>
    <li><svg width="18" height="16" viewBox="0 0 18 16"><rect x="1" y="3" width="12" height="12" fill="none" stroke="#f2513d" stroke-width="1.6"/><path d="M4 8l3 3 9-10" fill="none" stroke="#f2513d" stroke-width="2"/></svg>Quis Nostrud Exercitation Ullamco Laboris Nisi Ut Aliquip Ex Ea Commodo Consequat. Duis Aute Irure Dolor In</li>
    <li><svg width="18" height="16" viewBox="0 0 18 16"><rect x="1" y="3" width="12" height="12" fill="none" stroke="#f2513d" stroke-width="1.6"/><path d="M4 8l3 3 9-10" fill="none" stroke="#f2513d" stroke-width="2"/></svg>Dolore Eu Fugiat Nulla Pariatur. Excepteur Sint Occaecat Cupidatat Non Proident, Sunt In Culpa Qui Officia Deserunt</li>
    <li><svg width="18" height="16" viewBox="0 0 18 16"><rect x="1" y="3" width="12" height="12" fill="none" stroke="#f2513d" stroke-width="1.6"/><path d="M4 8l3 3 9-10" fill="none" stroke="#f2513d" stroke-width="2"/></svg>Sed Ut Perspiciatis Unde Omnis Iste Natus Error Sit Voluptatem Accusantium Doloremque Laudantium, Totam Rem</li>
  </ul>
  <a class="btn btn--blue" href="#" style="left:161px;top:442px;width:126px;height:35px">Contact Us</a>
  <div class="abs video">
    <div class="video__screen" role="img" aria-label="Video still of two students writing at a classroom desk">
      <svg class="abs" style="left:172px;top:122px" width="52" height="52" viewBox="0 0 52 52"><circle cx="26" cy="26" r="23" fill="rgba(0,0,0,.25)" stroke="#fff" stroke-width="3"/><path d="M21 15l16 11-16 11z" fill="#fff"/></svg>
      <div class="video__bar">
        <svg class="abs" style="left:6px;top:6px" width="30" height="18" viewBox="0 0 30 18"><rect width="30" height="18" fill="#333"/><path d="M12 5l8 4-8 4z" fill="#fff"/></svg>
        <div class="abs" style="left:60px;top:13px;width:260px;height:4px;background:#777"><div style="width:20px;height:4px;background:#fff"></div></div>
        <span class="abs" style="left:336px;top:8px;font-size:11px;color:#fff;font-weight:700;font-style:italic">◂)) HD</span>
        <svg class="abs" style="left:384px;top:8px" width="14" height="14" viewBox="0 0 14 14"><path d="M1 1l4 4M13 1l-4 4M1 13l4-4M13 13l-4-4" stroke="#fff" stroke-width="2"/></svg>
      </div>
    </div>
  </div>
</section>

<section class="who">
  <div class="framed" style="left:162px;top:78px">
    <div class="framed__back" style="left:0;top:12px;width:326px;height:275px"></div>
    <div class="framed__img" role="img" aria-label="Photo of a student holding books in a busy classroom" style="left:12px;top:0;width:327px;height:272px;background:linear-gradient(120deg,#3a3f4a 0%,#cfd3d6 40%,#f2f2f0 55%,#4a5a6a 100%)"></div>
  </div>
  <h2 class="heading">Who are BRV Remote Learning</h2>
  <p style="top:112px">BRV Remote Learning Has Been Providing Distance Education For Over <span>40 Years</span> And Have Been The Leader In Online Education For Over <span>25 Years</span>.</p>
  <p style="top:167px">Benefit From The Resources And Experience Of One Of The Worlds Leading Course Content Providers.</p>
  <p style="top:227px">Our Highly Qualified Academic Staff, HUGE Resource Library Of Up To Date Courses And Cutting Edge White Label LMS Enable Our Affiliates To Stay Well Ahead Of Their Competitors</p>
  <a class="btn btn--red" href="#" style="left:543px;top:309px;width:248px;height:36px">More About BRV Remote Learning</a>
</section>

<section class="interested">
  <h2 class="heading center" style="top:70px">Interested in becoming an affiliate?</h2>
  <p class="abs center" style="top:113px;font-size:13px;line-height:20px;color:var(--ink)">Contact Us Now To Discuss How We Can Work Together<br>To Launch Your Own Distance Education Business...</p>
  <svg class="abs" style="left:832px;top:92px" width="50" height="110" viewBox="0 0 50 110"><path d="M8 5c30 5 40 35 25 55-8 10-20 5-14-5 6-8 20 5 10 25-4 8-12 14-20 18" fill="none" stroke="#9a9a9a" stroke-width="1.4" stroke-dasharray="4 3"/><path d="M4 96l5 2-1 6" fill="none" stroke="#9a9a9a" stroke-width="1.4"/></svg>
  <div class="lead-form">
    <div class="lead-form__field"><svg width="10" height="10" viewBox="0 0 10 10"><path d="M1 5l8-4-4 8-1-3z" fill="none" stroke="#666"/></svg>Education Business</div>
    <div class="lead-form__submit"><svg width="10" height="10" viewBox="0 0 10 10"><path d="M1 5l8-4-4 8-1-3z" fill="none" stroke="#fff"/></svg>Now To Discuss</div>
  </div>
  <p class="abs center" style="top:209px;font-size:13px;color:var(--ink)">OR CALL US AT 555-010-2738</p>
</section>

<section class="why">
  <h2 class="heading center" style="top:70px">Why choose us</h2>
  <p class="abs center" style="top:113px;font-size:12.5px;line-height:20px;font-weight:700;color:var(--ink)">Lorem Ipsum Dolor Sit Amet, Consectetur Adipiscing Elit, Sed Do<br>Incididunt Ut Labore Et Dolore Magna Aliqua</p>

  <div class="feature feature--active" style="left:161px">
    <svg width="46" height="44" viewBox="0 0 46 44"><rect x="2" y="4" width="42" height="28" rx="2" fill="none" stroke="#2b2f3a" stroke-width="2"/><path d="M17 32l-3 9h18l-3-9M10 41h26" fill="none" stroke="#2b2f3a" stroke-width="2"/><path d="M14 16l9-5 9 5-9 5z" fill="#f2513d"/><path d="M17 18v5c3 2 9 2 12 0v-5" fill="none" stroke="#2b2f3a" stroke-width="1.5"/></svg>
    <span class="feature__label">Delivering Our<br>Courses</span>
  </div>
  <div class="feature" style="left:482px">
    <svg width="48" height="44" viewBox="0 0 48 44"><path d="M3 14v26c8-3 14-3 21 0 7-3 13-3 21 0V14" fill="none" stroke="#2b2f3a" stroke-width="2"/><path d="M24 18v22" stroke="#2b2f3a" stroke-width="2"/><circle cx="24" cy="12" r="10" fill="#fff" stroke="#2b2f3a" stroke-width="2"/><text x="24" y="17" text-anchor="middle" font-family="Lato,sans-serif" font-weight="700" font-size="13" fill="#2b2f3a">E</text></svg>
    <span class="feature__label">Selling Our<br>Ebooks</span>
  </div>
  <div class="feature" style="left:801px">
    <svg width="44" height="46" viewBox="0 0 44 46"><circle cx="22" cy="15" r="9" fill="none" stroke="#2b2f3a" stroke-width="2"/><path d="M11 15a11 11 0 0 1 22 0" fill="none" stroke="#2b2f3a" stroke-width="2"/><rect x="8" y="13" width="4" height="7" fill="#f2513d"/><rect x="32" y="13" width="4" height="7" fill="#f2513d"/><path d="M4 44c0-10 8-16 18-16s18 6 18 16z" fill="none" stroke="#2b2f3a" stroke-width="2"/></svg>
    <span class="feature__label">Extra Support<br>Available</span>
  </div>

  <h3 class="abs why__title">Delivering Our Courses</h3>
  <p class="abs why__copy">Systems Allow Delivery Online, On USB Stick Or With Printed Notes.Over 600 Courses, Over 25 Million Words Of Intellectual Property. Latest Course Versions Accessed Via A Cloud Based Repository Royalties Paid Monthly</p>
  <a class="btn btn--red" href="#" style="left:163px;top:522px;width:125px;height:33px">Contact Us</a>
  <div class="abs why__image" role="img" aria-label="Photo of a team of colleagues gathered around a laptop"></div>
</section>

<section class="contact">
  <h2 class="abs center contact__title">GET IN TOUCH</h2>
  <p class="abs center contact__sub">Get free access to our info packes</p>
  <div class="field" style="left:258px;top:164px;width:331px"><svg width="12" height="13" viewBox="0 0 12 13"><circle cx="6" cy="4" r="3" fill="none" stroke="#4a78c8"/><path d="M1 12c0-4 10-4 10 0z" fill="none" stroke="#4a78c8"/></svg>First Name</div>
  <div class="field" style="left:610px;top:164px;width:332px"><svg width="12" height="13" viewBox="0 0 12 13"><circle cx="6" cy="4" r="3" fill="none" stroke="#4a78c8"/><path d="M1 12c0-4 10-4 10 0z" fill="none" stroke="#4a78c8"/></svg>Last Name</div>
  <div class="field" style="left:258px;top:223px;width:331px"><svg width="14" height="11" viewBox="0 0 14 11"><rect x="1" y="1" width="12" height="9" fill="none" stroke="#4a78c8"/><path d="M1 1l6 5 6-5" fill="none" stroke="#4a78c8"/></svg>Email</div>
  <div class="field" style="left:610px;top:223px;width:332px"><svg width="13" height="13" viewBox="0 0 13 13"><path d="M2 1l3 0 1 3-2 1c1 2 2 3 4 4l1-2 3 1v3c-6 0-11-5-10-10z" fill="none" stroke="#4a78c8"/></svg>Phone</div>
  <div class="field field--message" style="left:258px;top:283px;width:684px;height:116px"><svg width="13" height="13" viewBox="0 0 13 13"><path d="M2 11l1-3 7-7 2 2-7 7z" fill="none" stroke="#4a78c8"/></svg>Message</div>
  <a class="btn btn--blue" href="#" style="left:534px;top:425px;width:132px;height:35px">Submit Now</a>
</section>

<footer class="site-footer">
  <div class="abs center footer-brand">
    <span>BRV Remote Learning</span>
    <span>Affiliate Program</span>
  </div>
  <nav class="abs center footer-nav">
    <span>ABOUT</span><span>OUR COURSES</span><span>LMS PLATFORM</span><span>AFFILIATE PROGRAM</span><span>CONTACT</span>
  </nav>
  <div class="abs footer-rule"></div>
  <p class="abs copyright">Copyright © 2021 BRV Remote Learning. All Rights Reserved. | Privacy Policy</p>
  <div class="abs socials" aria-label="Social links"><span></span><span></span><span></span><span></span></div>
</footer>

</body>
</html>
```